Heron Ridge Distillery Bottle Label Design

We need a label design for a product called "Coldwater Mill Straight Bourbon Whiskey". The bottle has two embossments on the side and an image printed on the back that will show through when looking from the front (shown in the attached image). It's made of 30% rye and 70% corn; images of the ingredients can be incorporated into the label design. We are a distillery that produces whiskey and bourbon from local farmers around the area. We focus on the quality of the ingredients and using the recipes passed down from generation to generation. We like a straight forward design using two colors maximum. The background will be brown once filled with the bourbon, so it must contrast against it (i.e. white and other lighter colors). The Heron Ridge Distillery logo must be present on the bottle front, as well as 750 ml, 84 PROOF, 42% ALC/VOL.

Target Market(s)

Craft whiskey consumers.

Industry/Entity Type

Product

Colors
fee18a
fbe7d2
fff3d1
fefcee
fefdec
fdf9cf

Requirements
Must have
• 750 ml, 84 PROOF, 42% ALC/VOL. Aged for 3 years.The Heron Ridge Distillery logo must be present on the bottle. Only two colors on label.
Nice to have
• Story of how we are a micro distillery making hand crafted whiskey.
Should not have
• False or misleading print.

```html
<!DOCTYPE html>
<html lang="en">
<head>
<meta charset="utf-8">
<title>Heron Ridge Distillery – Coldwater Mill Straight Bourbon Whiskey Label</title>
<link rel="stylesheet" href="https://fonts.googleapis.com/css2?family=Roboto+Slab:wght@700;800&family=Pinyon+Script&family=PT+Sans+Narrow:wght@400;700&display=swap">
<style>
  :root {
    --backdrop: #120a05;
    --label-gold: #fee18a;
    --label-cream: #fff3d1;
    --label-light: #fefcee;
    --ink-brown: #4a2814;
    --ink-dark: #3a1f0f;
    --backing-brown: #5a3420;
    --banner-gold: #fee18a;
    --banner-cream: #fefdec;
  }
  * { margin: 0; padding: 0; box-sizing: border-box; }
  html, body {
    width: 1200px;
    height: 3175px;
    overflow: hidden;
    background: var(--backdrop);
  }
  .label {
    position: relative;
    width: 1200px;
    height: 3175px;
  }
  .label-shapes {
    position: absolute;
    inset: 0;
  }
  .label-text {
    position: absolute;
    left: 0;
    width: 1200px;
    text-align: center;
    color: var(--ink-brown);
  }
  .brand-mark {
    position: absolute;
    left: 555px;
    top: 410px;
    width: 90px;
    height: 90px;
    border-radius: 50%;
    background: var(--ink-brown);
  }
  .brand-name {
    top: 518px;
    font-family: "Roboto Slab", serif;
    font-weight: 700;
    font-size: 74px;
    line-height: 84px;
  }
  .brand-sub {
    top: 620px;
    font-family: "Roboto Slab", serif;
    font-weight: 700;
    font-size: 34px;
    line-height: 40px;
    letter-spacing: 8px;
  }
  .product-script {
    top: 750px;
    font-family: "Pinyon Script", cursive;
    font-size: 84px;
    line-height: 100px;
  }
  .banner-title {
    top: 1200px;
    font-family: "Roboto Slab", serif;
    font-weight: 800;
    letter-spacing: 10px;
    line-height: 1;
  }
  .banner-title .line-bourbon {
    display: block;
    font-size: 150px;
    color: var(--banner-gold);
  }
  .banner-title .line-whiskey {
    display: block;
    margin-top: 22px;
    font-size: 150px;
    color: var(--banner-cream);
  }
  .grain-art {
    position: absolute;
    left: 420px;
    top: 1660px;
    width: 360px;
    height: 290px;
    border-radius: 40px;
    background: radial-gradient(ellipse at center, #8a5a34 0%, #b88a52 55%, rgba(254, 225, 138, 0) 80%);
  }
  .tagline {
    top: 1985px;
    font-family: "PT Sans Narrow", sans-serif;
    font-weight: 400;
    font-size: 64px;
    line-height: 74px;
    letter-spacing: 3px;
  }
  .volume {
    position: absolute;
    left: 315px;
    top: 2250px;
    font-family: "Roboto Slab", serif;
    font-weight: 700;
    font-size: 50px;
    color: var(--ink-brown);
  }
  .strength {
    position: absolute;
    left: 555px;
    top: 2262px;
    font-family: "PT Sans Narrow", sans-serif;
    font-weight: 700;
    font-size: 30px;
    color: var(--ink-brown);
  }
  .aging {
    top: 2350px;
    font-family: "PT Sans Narrow", sans-serif;
    font-weight: 700;
    font-size: 36px;
    line-height: 44px;
    letter-spacing: 4px;
  }
  .contact {
    top: 2500px;
    font-family: "PT Sans Narrow", sans-serif;
    font-style: normal;
    font-size: 34px;
    line-height: 46px;
  }
</style>
</head>
<body>
<main class="label">
  <svg class="label-shapes" width="1200" height="3175" viewBox="0 0 1200 3175" aria-hidden="true">
    <defs>
      <radialGradient id="label-fill" cx="50%" cy="55%" r="65%">
        <stop offset="0" stop-color="#fff3d1"/>
        <stop offset="0.6" stop-color="#fee9a4"/>
        <stop offset="1" stop-color="#fee18a"/>
      </radialGradient>
    </defs>
    <path class="label-backing" d="M168 940 L1032 940 L1032 2350 L168 2350 Z" fill="var(--backing-brown)"/>
    <path class="label-body" d="M250 300 L950 300 L980 330 L980 2663 L600 2888 L220 2663 L220 330 Z"
          fill="var(--ink-dark)"/>
    <path class="label-face" d="M262 318 L938 318 L962 342 L962 2652 L600 2866 L238 2652 L238 342 Z"
          fill="url(#label-fill)"/>
    <path class="label-inner-rule" d="M272 336 L928 336 L944 352 L944 2640 L600 2844 L256 2640 L256 352 Z"
          fill="none" stroke="var(--ink-brown)" stroke-width="8"/>
    <line class="brand-rule" x1="430" y1="614" x2="770" y2="614" stroke="var(--ink-brown)" stroke-width="4"/>
    <line class="brand-rule" x1="430" y1="670" x2="770" y2="670" stroke="var(--ink-brown)" stroke-width="4"/>
    <path class="title-banner" d="M151 1205 Q600 1120 1065 1205 L1065 1600 Q600 1660 151 1600 Z"
          fill="var(--ink-dark)"/>
    <path d="M175 1228 Q600 1146 1041 1228 L1041 1578 Q600 1634 175 1578 Z"
          fill="none" stroke="var(--banner-gold)" stroke-width="8"/>
    <line x1="430" y1="1968" x2="770" y2="1968" stroke="var(--ink-brown)" stroke-width="4"/>
    <line x1="430" y1="2170" x2="770" y2="2170" stroke="var(--ink-brown)" stroke-width="4"/>
    <line x1="330" y1="2660" x2="870" y2="2660" stroke="var(--ink-brown)" stroke-width="3"/>
  </svg>

  <span class="brand-mark" aria-hidden="true"></span>
  <div class="label-text brand-name">Heron Ridge</div>
  <div class="label-text brand-sub">DISTILLERY</div>
  <div class="label-text product-script">Coldwater Mill<br>Straight</div>

  <h1 class="label-text banner-title">
    <span class="line-bourbon">BOURBON</span>
    <span class="line-whiskey">WHISKEY</span>
  </h1>

  <div class="grain-art" role="img" aria-label="Illustration of corn cobs and rye stalks"></div>

  <div class="label-text tagline">HAND CRAFTED<br>WHISKEY</div>

  <div class="volume">750ml.</div>
  <div class="strength">84 PROOF - 42% Alc / Vol</div>
  <div class="label-text aging">AGED FOR 3 YEARS</div>

  <address class="label-text contact">
    418 Mill Pond Road, Alder Falls, MN 55901<br>
    Tel: (555) 014-2290<br>
    E-mail: heronridgedistillery@example.com
  </address>
</main>
</body>
</html>
```